Social Media Template Design for a leading Veterinary Clinic in Austria

We are looking for social media design templates including the following:
- single picture posting (Snapvale & KL)
- carousel postings (Snapvale)
- story (Snapvale & KL)
- reel thumbnail (Snapvale & KL)
- story highlight design (Snapvale)

What are the templates for?
We are working on a way to make posting content more efficient. Therefore, we'd like to use templates for a more efficient content creation in the future. In this way on the one hand, we expect creating different kind of content to be easier and faster, on the other it should create consistency throughout our channels.. We work with Adobe CC and mostly use Photoshop or Indesign for content creation.

How should they look?
The two strongest colors of our CI are dark blue and gold. We expect templates in which these colors are the unifying element. We think that our logo does not have to appear. Our brand identity is modern, clean, professional, revolutionary and yet inviting. Our social presence should also convey this impression. Our postings contain images and text. As an example for template use, we plan on introducing our employees - here we would have to use the employee's photo and insert title and name.

At the moment it is hard to tell how many designs we will need in total, as we might need to adapt or extend the template after the first use cases.
But for the start we'd aprox. expect:
- 2-3 different story slides
- 3 carousel slides
- 1 reel thumbnail
- 1 story highlight design, in which we can adapt the icons on our own

Do you think, you can help us out?

Already looking forward to your design ideas! 😊 Feel free to contact us for any further questions.

Target Market(s)

Austria

Industry/Entity Type

Veterinary Medicine

Font styles to use
Serif
Sans Serif

Colors

Designer to choose colors to be used in the design.

Requirements
Must have
• templates for Adobe Photoshop or InDesign in formats 1:1, 9:16, 4:5 according to content (story, posting, reel etc.) and channel
Should not have
• ready-to-post content, content ideas - only templates we can fill with content

```html
<!DOCTYPE html>
<html lang="de">
<head>
<meta charset="utf-8">
<title>Tierklinik Social Media Templates</title>
<link rel="stylesheet" href="https://fonts.googleapis.com/css2?family=Playfair+Display:wght@600;700&family=Montserrat:wght@400;600;800&display=swap">
<style>
:root{
  --navy:#1d3150;
  --navy-dark:#15243d;
  --gold:#e2a62a;
  --gold-light:#f1c766;
  --white:#ffffff;
  --board:#ececee;
  --ink:#2a2f3a;
  --photo-a:#8a96a8;
  --photo-b:#c9ced6;
}
*{box-sizing:border-box;margin:0;padding:0}
html,body{width:849px;height:1200px;overflow:hidden}
body{background:var(--board);font-family:"Montserrat",sans-serif;color:var(--ink);position:relative}
.board-shape{position:absolute;inset:0}
.label{position:absolute;font-weight:800;font-size:11px;letter-spacing:.5px;color:var(--ink)}
.abs{position:absolute}
.photo{position:absolute;background:linear-gradient(150deg,var(--photo-b),var(--photo-a))}
.photo.warm{background:linear-gradient(150deg,#d9c7a8,#6f6a62)}
.photo.dog{background:linear-gradient(160deg,#3b3a3a,#b8aa94)}
.photo.team{background:linear-gradient(160deg,#5c6f8c,#a7b3c4)}
.serif{font-family:"Playfair Display",serif}

/* feed post */
.feed-post{left:45px;top:40px;width:295px;height:295px;background:var(--white);overflow:hidden}
.feed-name{left:0;right:0;top:200px;text-align:center;font-size:20px;color:var(--navy)}
.feed-role{left:0;right:0;top:228px;text-align:center;font-size:9px;color:var(--gold);font-weight:600}
.feed-cta{left:95px;top:270px;width:105px;height:16px;color:var(--white);font-size:6.5px;text-align:center;line-height:16px}
.variant-num{font-weight:800;font-size:10px;color:var(--ink)}
.variant{width:155px;height:150px;overflow:hidden;background:var(--navy)}

/* carousel */
.carousel{left:50px;top:385px;width:750px;height:160px;overflow:hidden;background:var(--navy)}
.slide{position:absolute;top:0;width:188px;height:160px;overflow:hidden}
.slide + .slide{border-left:1px solid rgba(255,255,255,.12)}
.slide-title{font-size:11px;line-height:1.15;color:var(--gold)}
.slide-text{font-size:6.5px;line-height:1.5;color:var(--white)}

/* stories */
.story{position:absolute;width:115px;overflow:hidden;background:var(--navy)}
.story-head{font-weight:800;font-size:8.5px;line-height:1.25;color:var(--white);text-align:center}
.bar{position:absolute;height:4px;background:rgba(255,255,255,.55);border-radius:2px}

/* reels */
.reel{position:absolute;width:115px;overflow:hidden;background:var(--navy)}
.reel-head{font-weight:800;font-size:9px;line-height:1.2;color:var(--white)}
.reel-head b{color:var(--gold)}

/* highlights */
.highlight{position:absolute;top:1142px;width:36px;height:36px;border-radius:50%;background:var(--navy);border:3px solid var(--gold)}
</style>
</head>
<body>

<svg class="board-shape" width="849" height="1200" aria-hidden="true">
  <polygon points="560,0 849,0 849,520 300,1200 0,1200 0,980" fill="#f7f7f8"/>
</svg>

<!-- FEED -->
<div class="label" style="left:50px;top:22px">FEED SNAPVALE</div>
<section class="abs feed-post">
  <svg class="abs" width="295" height="295" style="left:0;top:0" aria-hidden="true">
    <path d="M0 0 H90 Q40 20 0 80 Z" fill="var(--gold)"/>
    <path d="M0 295 V265 Q150 240 295 268 V295 Z" fill="var(--navy)"/>
    <circle cx="147" cy="105" r="78" fill="var(--gold)"/>
  </svg>
  <div class="photo warm" role="img" aria-label="Portraitfoto der Tierärztin" style="left:75px;top:33px;width:144px;height:144px;border-radius:50%"></div>
  <div class="abs feed-name serif">Dr. Lena Hofbauer</div>
  <div class="abs feed-role">Tierärztin für Kleintiere</div>
  <div class="abs feed-cta">Termin online buchen</div>
</section>

<div class="abs variant-num" style="left:416px;top:30px">(1)</div>
<div class="abs variant-num" style="left:581px;top:30px">(2)</div>
<div class="abs variant-num" style="left:746px;top:30px">(3)</div>

<div class="abs variant" style="left:350px;top:45px">
  <div class="photo team" role="img" aria-label="Teamfoto der Klinik" style="left:6px;top:6px;width:143px;height:120px"></div>
  <svg class="abs" style="left:0;top:118px" width="155" height="32" aria-hidden="true"><path d="M0 10 Q78 -4 155 12 V32 H0Z" fill="var(--gold)"/></svg>
</div>
<div class="abs variant" style="left:515px;top:45px">
  <div class="photo team" role="img" aria-label="Teamfoto der Klinik" style="left:6px;top:6px;width:143px;height:120px"></div>
  <svg class="abs" style="left:0;top:118px" width="155" height="32" aria-hidden="true"><path d="M0 16 Q78 2 155 16 V32 H0Z" fill="var(--gold)"/></svg>
</div>
<div class="abs variant" style="left:680px;top:45px">
  <div class="photo team" role="img" aria-label="Teamfoto der Klinik" style="left:6px;top:6px;width:143px;height:120px"></div>
  <svg class="abs" style="left:0;top:118px" width="155" height="32" aria-hidden="true"><path d="M0 20 Q78 6 155 14 V32 H0Z" fill="var(--gold)"/></svg>
</div>

<div class="abs variant" style="left:350px;top:198px;height:140px">
  <div class="photo dog" role="img" aria-label="Foto eines Hundes" style="left:6px;top:6px;width:143px;height:110px"></div>
</div>
<div class="abs variant" style="left:515px;top:198px;height:140px">
  <div class="photo dog" role="img" aria-label="Foto eines Hundes" style="left:6px;top:6px;width:143px;height:110px"></div>
</div>
<div class="abs variant" style="left:680px;top:198px;height:140px">
  <div class="photo dog" role="img" aria-label="Foto eines Hundes" style="left:6px;top:6px;width:143px;height:110px"></div>
</div>

<!-- CAROUSEL -->
<div class="label" style="left:375px;top:360px">CAROUSEL SLIDES</div>
<section class="abs carousel">
  <div class="slide" style="left:0;background:var(--white)">
    <svg class="abs" width="188" height="160" aria-hidden="true">
      <circle cx="38" cy="38" r="30" fill="var(--gold)"/>
      <rect x="0" y="150" width="188" height="10" fill="var(--navy)"/>
    </svg>
    <div class="photo warm" role="img" aria-label="Foto eines Tieres in der Adventszeit" style="left:14px;top:14px;width:48px;height:48px;border-radius:50%"></div>
    <div class="abs serif" style="left:14px;top:82px;width:160px;font-size:17px;line-height:1.1;color:var(--navy)">Gefahren Während der Adventszeit</div>
  </div>
  <div class="slide" style="left:188px">
    <div class="abs slide-title serif" style="left:12px;top:14px;width:160px">Gefahren Während der Adventszeit</div>
    <div class="abs slide-text" style="left:12px;top:48px;width:95px">Kerzen, Schokolade und Lametta bergen Risiken für Tiere.</div>
    <svg class="abs" width="188" height="160" aria-hidden="true"><circle cx="145" cy="110" r="34" fill="var(--gold)"/></svg>
    <div class="photo" role="img" aria-label="Foto eines Adventsgestecks" style="left:116px;top:81px;width:58px;height:58px;border-radius:50%"></div>
  </div>
  <div class="slide" style="left:376px">
    <div class="abs slide-title serif" style="left:12px;top:14px;width:160px">Gefahren Während der Adventszeit</div>
    <div class="abs slide-text" style="left:12px;top:48px;width:95px">Giftpflanzen wie Weihnachtsstern gehören außer Reichweite.</div>
    <svg class="abs" width="188" height="160" aria-hidden="true"><circle cx="45" cy="118" r="30" fill="var(--gold)"/></svg>
    <div class="photo warm" role="img" aria-label="Foto einer Katze" style="left:20px;top:93px;width:50px;height:50px;border-radius:50%"></div>
  </div>
  <div class="slide" style="left:564px">
    <svg class="abs" width="188" height="160" aria-hidden="true"><path d="M188 0 V110 H80 Q70 40 188 0Z" fill="var(--gold)"/></svg>
    <div class="photo dog" role="img" aria-label="Foto eines Hundes" style="left:90px;top:0;width:98px;height:100px;border-radius:0 0 0 50px"></div>
    <div class="abs slide-title serif" style="left:12px;top:122px;width:165px">Lorem Ipsum dolor sit</div>
  </div>
</section>

<!-- STORIES -->
<div class="label" style="left:50px;top:572px">SNAPVALE STORY</div>
<div class="story" style="left:50px;top:595px;height:250px;background:var(--white)">
  <svg class="abs" width="115" height="250" aria-hidden="true">
    <circle cx="57" cy="70" r="48" fill="var(--gold)"/>
    <path d="M0 150 Q58 130 115 150 V250 H0Z" fill="var(--navy)"/>
  </svg>
  <div class="photo warm" role="img" aria-label="Foto einer Katze" style="left:17px;top:30px;width:80px;height:80px;border-radius:50%"></div>
  <div class="abs story-head" style="left:8px;right:8px;top:172px">LOREM IPSUM DOLOR SIT AMET</div>
  <div class="abs" style="left:30px;top:212px;width:55px;height:12px;border-radius:6px;background:var(--gold);font-size:5.5px;font-weight:600;text-align:center;line-height:12px;color:var(--navy)">Mehr erfahren</div>
</div>
<div class="story" style="left:180px;top:595px;height:250px">
  <div class="photo" role="img" aria-label="Foto eines Behandlungsraums" style="left:0;top:0;width:115px;height:120px"></div>
  <svg class="abs" style="top:105px" width="115" height="30" aria-hidden="true"><path d="M0 12 Q58 -4 115 12 V30 H0Z" fill="var(--gold)"/></svg>
  <div class="abs story-head" style="left:8px;right:8px;top:150px">LOREM IPSUM DOLOR SIT AMET, CONSECTETUR</div>
</div>
<div class="story" style="left:310px;top:595px;height:250px">
  <div class="abs story-head" style="left:8px;right:8px;top:30px;color:var(--gold)">LOREM IPSUM DOLOR SIT AMET, CONSECTETUR</div>
  <div class="photo dog" role="img" aria-label="Foto eines Hundes" style="left:12px;top:90px;width:91px;height:110px;border-radius:45px 45px 0 0"></div>
  <svg class="abs" style="top:215px" width="115" height="35" aria-hidden="true"><path d="M0 14 Q58 0 115 14 V35 H0Z" fill="var(--gold)"/></svg>
</div>

<div class="story" style="left:50px;top:865px;height:280px">
  <svg class="abs" width="115" height="280" aria-hidden="true">
    <path d="M0 0 H115 V30 Q58 50 0 30Z" fill="var(--gold)"/>
    <path d="M0 250 Q58 235 115 250 V280 H0Z" fill="var(--gold)"/>
  </svg>
  <div class="abs story-head" style="left:8px;right:8px;top:110px">LOREM IPSUM DOLOR SIT AMET, CONSECTETUR</div>
</div>
<div class="story" style="left:180px;top:865px;height:280px">
  <div class="abs serif" style="left:12px;top:24px;width:91px;height:130px;background:var(--white);text-align:center;padding-top:22px;font-size:22px;color:var(--navy)">Q&amp;A</div>
  <div class="abs" style="left:22px;top:90px;width:71px;height:40px;border:1px solid var(--navy);font-size:6px;text-align:center;padding-top:15px;color:var(--navy)">Stell uns deine Frage</div>
  <svg class="abs" style="top:245px" width="115" height="35" aria-hidden="true"><path d="M0 14 Q58 0 115 14 V35 H0Z" fill="var(--gold)"/></svg>
</div>
<div class="story" style="left:310px;top:865px;height:280px">
  <div class="abs story-head" style="left:8px;right:8px;top:24px;color:var(--gold)">LOREM IPSUM DOLOR SIT AMET</div>
  <div class="bar" style="left:14px;top:70px;width:87px"></div>
  <div class="bar" style="left:14px;top:82px;width:70px"></div>
  <div class="bar" style="left:14px;top:104px;width:87px"></div>
  <div class="bar" style="left:14px;top:116px;width:60px"></div>
  <div class="bar" style="left:14px;top:138px;width:87px"></div>
  <div class="bar" style="left:14px;top:150px;width:74px"></div>
  <div class="bar" style="left:14px;top:172px;width:87px"></div>
  <div class="bar" style="left:14px;top:184px;width:50px"></div>
  <svg class="abs" style="top:245px" width="115" height="35" aria-hidden="true"><path d="M0 14 Q58 0 115 14 V35 H0Z" fill="var(--gold)"/></svg>
</div>

<!-- REELS -->
<div class="label" style="left:495px;top:572px">REEL THUMBNAIL</div>
<div class="reel" style="left:435px;top:598px;height:252px">
  <div class="photo warm" role="img" aria-label="Foto einer Mitarbeiterin" style="left:0;top:0;width:115px;height:150px"></div>
  <svg class="abs" style="top:138px" width="115" height="20" aria-hidden="true"><path d="M0 8 Q58 -4 115 8 V20 H0Z" fill="var(--gold)"/></svg>
  <div class="abs reel-head" style="left:10px;top:175px;width:95px">LOREM IPSUM <b>DOLOR SIT AMET,</b> CONSECTETUR</div>
</div>
<div class="reel" style="left:560px;top:598px;height:252px">
  <div class="photo warm" role="img" aria-label="Foto einer Mitarbeiterin" style="left:0;top:0;width:115px;height:150px"></div>
  <svg class="abs" style="top:138px" width="115" height="20" aria-hidden="true"><path d="M0 12 Q58 -2 115 4 V20 H0Z" fill="var(--gold)"/></svg>
  <div class="abs reel-head" style="left:10px;top:175px;width:95px">LOREM IPSUM <b>DOLOR SIT AMET,</b> CONSECTETUR</div>
</div>
<div class="reel" style="left:685px;top:598px;height:252px">
  <div class="photo warm" role="img" aria-label="Foto einer Mitarbeiterin" style="left:0;top:0;width:115px;height:150px"></div>
  <svg class="abs" style="top:138px" width="115" height="20" aria-hidden="true"><path d="M0 4 Q58 14 115 6 V20 H0Z" fill="var(--gold)"/></svg>
  <div class="abs reel-head" style="left:10px;top:175px;width:95px">LOREM IPSUM <b>DOLOR SIT AMET,</b> CONSECTETUR</div>
</div>

<div class="reel" style="left:435px;top:865px;height:210px">
  <svg class="abs" width="115" height="210" aria-hidden="true">
    <path d="M0 0 H115 V26 Q58 48 0 26Z" fill="var(--gold)"/>
    <path d="M0 185 Q58 170 115 185 V210 H0Z" fill="var(--gold)"/>
  </svg>
  <div class="abs reel-head" style="left:10px;top:80px;width:95px">LOREM IPSUM <b>DOLOR SIT AMET,</b> CONSECTETUR</div>
</div>
<div class="reel" style="left:560px;top:865px;height:210px">
  <svg class="abs" width="115" height="210" aria-hidden="true">
    <path d="M0 0 H115 V18 Q58 44 0 30Z" fill="var(--gold)"/>
    <path d="M0 180 Q58 195 115 178 V210 H0Z" fill="var(--gold)"/>
  </svg>
  <div class="abs reel-head" style="left:10px;top:80px;width:95px">LOREM IPSUM <b>DOLOR SIT AMET,</b> CONSECTETUR</div>
</div>
<div class="reel" style="left:685px;top:865px;height:210px">
  <svg class="abs" width="115" height="210" aria-hidden="true">
    <path d="M0 0 H115 V32 Q58 20 0 36Z" fill="var(--gold)"/>
    <path d="M0 188 Q58 172 115 190 V210 H0Z" fill="var(--gold)"/>
  </svg>
  <div class="abs reel-head" style="left:10px;top:80px;width:95px">LOREM IPSUM <b>DOLOR SIT AMET,</b> CONSECTETUR</div>
</div>

<!-- HIGHLIGHTS -->
<div class="label" style="left:470px;top:1115px">STORY HIGHLIGHT DESIGN</div>
<div class="highlight" style="left:470px"></div>
<div class="highlight" style="left:515px"></div>
<div class="highlight" style="left:560px"></div>
<div class="highlight" style="left:605px"></div>

</body>
</html>
```